Flair Bartenders Website Needs an Overhaul

We are a group of flair bartenders based in San Diego that provide a fun bartending alternative to private parties and events. We haven’t changed our website design in a long time and need to bring our current flash based website in line with the times and go to HTML5 (see our website www.pourvortexcrew.com).

We have a “skateboard grunge” theme to our current website and would like to keep that look as our pictures and video are all taken in an urban setting. We are not married to any particular colors and want to have a “rock star” feel to the site as it needs to attract people that like to party!

Find in the files our logo and the font file.
Updates

Target Market(s)

Our clients are fun, outgoing individuals where normal lines are blurred and risks are taken.

Industry/Entity Type

Events

Number of Pages Required

4 page

Requirements
Must have
• An urban skateboarding feel.
Nice to have
• Keep the green theme, although not essential.
Should not have
• No "business type" "corporate" websites.. BORING!!

```html
<!DOCTYPE html>
<html lang="en">
<head>
<meta charset="utf-8">
<title>Pour Vortex Crew</title>
<link rel="stylesheet" href="https://fonts.googleapis.com/css2?family=Raleway:wght@500;600;800&family=Open+Sans:wght@400;600&family=PT+Serif:wght@700&display=swap">
<style>
:root{
  --paper:#e9e9e9;
  --night:#0f0f0f;
  --footer:#1f1f1f;
  --ink:#111;
  --grey-text:#6b6b6b;
  --white:#fff;
  --muted:#c9c9c9;
  --orange:#f7941d;
  --lime:#b7d334;
  --mint:#2fd68a;
  --rule:#3a3a3a;
}
*{margin:0;padding:0;box-sizing:border-box}
html,body{width:1200px;height:1158px;overflow:hidden;background:var(--night)}
body{position:relative;font-family:"Open Sans",sans-serif;color:var(--white)}
.backdrop{position:absolute;left:0;top:0}
.side-photo{position:absolute;left:0;top:6px;width:200px;height:514px;background:linear-gradient(90deg,rgba(150,150,150,.55),rgba(200,200,200,.4) 65%,rgba(233,233,233,0));}
.brand{position:absolute;left:200px;top:40px;font-family:"Raleway",sans-serif;font-weight:800;font-size:50px;color:var(--ink);letter-spacing:-1px}
.enquiry{position:absolute;right:194px;top:78px;text-align:right;font-family:"Raleway",sans-serif}
.enquiry-label{font-size:15px;color:var(--grey-text);font-weight:500}
.enquiry-phone{font-size:23px;color:var(--ink);font-weight:500;display:flex;align-items:center;gap:4px;margin-top:1px}
.main-nav{position:absolute;left:192px;top:135px;width:816px;height:45px;display:flex;background:linear-gradient(#3a3a3a,#1c1c1c)}
.main-nav a{font-family:"PT Serif",serif;font-weight:700;font-size:13px;color:var(--white);text-decoration:none;display:flex;align-items:center;justify-content:center;border-right:1px solid #4a4a4a;letter-spacing:.3px}
.main-nav a:last-child{border-right:none}
.main-nav a.active{background:#0a0a0a}
.hero{position:absolute;left:192px;top:180px;width:816px;height:404px;filter:drop-shadow(0 10px 10px rgba(0,0,0,.75))}
.feature{position:absolute;top:636px;width:250px}
.feature h2{font-family:"Raleway",sans-serif;font-weight:600;font-size:18px;margin-bottom:7px;white-space:nowrap}
.feature p{font-size:9.5px;line-height:14px;color:var(--muted)}
.feature a{display:inline-block;margin-top:10px;font-family:"Raleway",sans-serif;font-weight:600;font-size:12.5px;color:var(--white);text-decoration:none}
.crew h2{color:var(--orange)}
.packages h2{color:var(--lime)}
.flair h2{color:var(--mint)}
.divider{position:absolute;left:193px;top:781px;width:814px;height:1px;background:var(--rule)}
.welcome{position:absolute;left:190px;top:838px;width:520px}
.welcome h1{font-family:"Raleway",sans-serif;font-weight:500;font-size:24px;margin-bottom:12px}
.welcome p{font-size:10px;line-height:14px;color:#e4e4e4;margin-bottom:7px;padding-left:3px}
.btn{display:inline-block;margin-top:7px;width:87px;height:26px;line-height:26px;text-align:center;background:var(--orange);color:var(--white);font-size:10px;text-decoration:none;border-radius:2px}
.video{position:absolute;left:735px;top:833px;width:271px;height:175px;border:4px solid var(--white);background:linear-gradient(120deg,#6d7a8a,#c9a27a 45%,#3a2a2a 80%,#1c1c1c)}
.play{position:absolute;left:50%;top:50%;transform:translate(-50%,-50%)}
.site-footer{position:absolute;left:0;top:1060px;width:1200px;height:98px;background:var(--footer)}
.footer-nav{position:absolute;left:195px;top:31px;font-family:"Raleway",sans-serif;font-weight:500;font-size:12.5px;color:var(--white)}
.footer-nav span{margin:0 6px}
.copyright{position:absolute;left:195px;top:54px;font-size:9.5px;color:#9a9a9a}
.social{position:absolute;right:205px;top:30px;display:flex;gap:10px}
.social span{width:16px;height:16px;border-radius:50%;background:var(--white)}
</style>
</head>
<body>
<svg class="backdrop" width="1200" height="1158" viewBox="0 0 1200 1158" aria-hidden="true">
  <defs>
    <linearGradient id="paper" x1="0" y1="0" x2="1" y2="1">
      <stop offset="0" stop-color="#dedede"/><stop offset=".6" stop-color="#ececec"/><stop offset="1" stop-color="#e2e2e2"/>
    </linearGradient>
    <filter id="blotch" x="0" y="0" width="100%" height="100%">
      <feTurbulence type="fractalNoise" baseFrequency="0.011" numOctaves="5" seed="7"/>
      <feColorMatrix type="matrix" values="0 0 0 0 0  0 0 0 0 0  0 0 0 0 0  2.2 0 0 0 -0.9"/>
    </filter>
    <filter id="grain" x="0" y="0" width="100%" height="100%">
      <feTurbulence type="fractalNoise" baseFrequency="0.9" numOctaves="2" seed="2"/>
      <feColorMatrix type="matrix" values="0 0 0 0 1  0 0 0 0 1  0 0 0 0 1  2 0 0 0 -1.1"/>
    </filter>
    <filter id="scuff" x="0" y="0" width="100%" height="100%">
      <feTurbulence type="fractalNoise" baseFrequency="0.02 0.006" numOctaves="4" seed="11"/>
      <feColorMatrix type="matrix" values="0 0 0 0 1  0 0 0 0 1  0 0 0 0 1  2.4 0 0 0 -1.2"/>
    </filter>
    <clipPath id="paperArea"><polygon points="0,0 1200,0 1200,522 1008,492 192,492 0,520"/></clipPath>
    <clipPath id="darkArea"><polygon points="0,520 192,492 1008,492 1200,522 1200,1060 0,1060"/></clipPath>
  </defs>
  <rect width="1200" height="1158" fill="#0f0f0f"/>
  <g clip-path="url(#darkArea)">
    <rect width="1200" height="1060" filter="url(#scuff)" opacity=".09"/>
    <rect width="1200" height="1060" filter="url(#grain)" opacity=".05"/>
  </g>
  <polygon points="0,0 1200,0 1200,522 1008,492 192,492 0,520" fill="url(#paper)"/>
  <g clip-path="url(#paperArea)">
    <rect width="1200" height="530" filter="url(#blotch)" opacity=".22"/>
    <rect width="1200" height="530" filter="url(#grain)" opacity=".5"/>
  </g>
  <rect width="1200" height="6" fill="#bdbdbd"/>
</svg>
<div class="side-photo" role="img" aria-label="Faded black and white photo of a bartender reaching forward"></div>

<header>
  <div class="brand">Pour Vortex Crew</div>
  <div class="enquiry">
    <div class="enquiry-label">FOR ENQUIRY</div>
    <div class="enquiry-phone">
      <svg width="18" height="18" viewBox="0 0 24 24" aria-hidden="true"><path fill="#111" d="M6.6 10.8a15.1 15.1 0 0 0 6.6 6.6l2.2-2.2a1 1 0 0 1 1-.25 11.4 11.4 0 0 0 3.6.57 1 1 0 0 1 1 1V20a1 1 0 0 1-1 1A17 17 0 0 1 3 4a1 1 0 0 1 1-1h3.5a1 1 0 0 1 1 1c0 1.250.2 2.450.57 3.570a1 1 0 0 1-.25 1z"/></svg>
      1.619.555.0147
    </div>
  </div>
  <nav class="main-nav">
    <a class="active" href="#" style="width:94px">HOME</a>
    <a href="#" style="width:109px">ABOUT US</a>
    <a href="#" style="width:103px">BOOKING</a>
    <a href="#" style="width:113px">PACKAGES</a>
    <a href="#" style="width:81px">CREW</a>
    <a href="#" style="width:86px">MEDIA</a>
    <a href="#" style="width:109px">FAN CLUB</a>
    <a href="#" style="width:121px">CONTACT</a>
  </nav>
</header>

<svg class="hero" width="816" height="404" viewBox="0 0 816 404" role="img" aria-label="Smiling flair bartender in bow tie and suspenders giving a thumbs up behind a bar">
  <defs>
    <radialGradient id="barGlow" cx=".5" cy=".45" r=".65">
      <stop offset="0" stop-color="#d9c4b0"/><stop offset=".3" stop-color="#8a5a3a"/><stop offset=".65" stop-color="#4a2a1a"/><stop offset="1" stop-color="#1e120c"/>
    </radialGradient>
    <pattern id="teethTop" x="0" y="0" width="7" height="6" patternUnits="userSpaceOnUse"><polygon points="0,6 3.5,0 7,6" fill="#fff"/></pattern>
    <pattern id="teethBottom" x="0" y="398" width="7" height="6" patternUnits="userSpaceOnUse"><polygon points="0,0 3.5,6 7,0" fill="#fff"/></pattern>
    <pattern id="teethLeft" x="0" y="0" width="6" height="7" patternUnits="userSpaceOnUse"><polygon points="6,0 0,3.5 6,7" fill="#fff"/></pattern>
    <pattern id="teethRight" x="810" y="0" width="6" height="7" patternUnits="userSpaceOnUse"><polygon points="0,0 6,3.5 0,7" fill="#fff"/></pattern>
    <mask id="tornEdge">
      <rect x="6" y="6" width="804" height="392" fill="#fff"/>
      <rect x="0" y="0" width="816" height="6" fill="url(#teethTop)"/>
      <rect x="0" y="398" width="816" height="6" fill="url(#teethBottom)"/>
      <rect x="0" y="0" width="6" height="404" fill="url(#teethLeft)"/>
      <rect x="810" y="0" width="6" height="404" fill="url(#teethRight)"/>
    </mask>
  </defs>
  <g mask="url(#tornEdge)">
    <rect width="816" height="404" fill="url(#barGlow)"/>
    <rect x="1" y="1" width="814" height="402" fill="none" stroke="#e8e8e8" stroke-width="2" stroke-dasharray="2 5" opacity=".8"/>
  </g>
  <g fill="#2a2a2a">
    <circle cx="384" cy="386" r="6"/><circle cx="400" cy="386" r="6"/><circle cx="416" cy="386" r="6"/><circle cx="432" cy="386" r="6"/>
  </g>
</svg>

<section class="feature crew" style="left:190px">
  <h2>OUR CREW</h2>
  <p>In massa libero interdum nec interdum vel blandit sed nulla In ullamcorper est eget tempor cursus neque mi consectetuer mi a ultricies massa est sed nisl Class aptent taciti ad litora torq</p>
  <a href="#">CLICK HERE &rsaquo;</a>
</section>
<section class="feature packages" style="left:473px">
  <h2>OUR PACKAGES</h2>
  <p>In massa libero interdum nec interdum vel blandit sed nulla In ullamcorper est eget tempor cursus neque mi consectetuer mi a ultricies massa est sed nisl Class aptent taciti ad litora torq</p>
  <a href="#">CLICK HERE &rsaquo;</a>
</section>
<section class="feature flair" style="left:757px">
  <h2>WHAT IS EXHIBITION FLAIR?</h2>
  <p>In massa libero interdum nec interdum vel blandit sed nulla In ullamcorper est eget tempor cursus neque mi consectetuer mi a ultricies massa est sed nisl Class aptent taciti ad litora torq</p>
  <a href="#">CLICK HERE &rsaquo;</a>
</section>

<div class="divider"></div>

<section class="welcome">
  <h1>Welcome to Pour Vortex Crew Mainpage</h1>
  <p>The Pour Vortex Crew are San Diego's top flair bartenders brought to your event and blended together with a dedication to service, mixology and entertainment. This is a fun alternative to traditional bartending that still provides great service with specialized personal crowd interaction plus an unbelievable flair show.</p>
  <p>Audiences are very receptive to this practical form of entertainment and it blends well in conjunction with live bands, DJs and fun events. The working package is most commonly requested with our bookings, and highly practical for both service and entertainment</p>
  <a class="btn" href="#">READ MORE</a>
</section>

<div class="video" role="img" aria-label="Video still of a bartender winking while tossing a bottle">
  <svg class="play" width="40" height="40" viewBox="0 0 40 40" aria-hidden="true"><circle cx="20" cy="20" r="19" fill="#fff"/><polygon points="16,12 16,28 28,20" fill="#111"/></svg>
</div>

<footer class="site-footer">
  <div class="footer-nav">HOME<span>|</span>ABOUT US<span>|</span>BOOKING<span>|</span>PACKAGES<span>|</span>CREW<span>|</span>MEDIA<span>|</span>FAN CLUB<span>|</span>CONTACT</div>
  <div class="copyright">© 2015 Company Name&nbsp; All right reserved&nbsp; Term of Use</div>
  <div class="social"><span aria-label="Social link"></span><span aria-label="Social link"></span><span aria-label="Social link"></span></div>
</footer>
</body>
</html>
```